Brightfern Couples Unity Program

We need a flyer that invites low-income Spanish speaking individuals to our program. The program is 12 weeks. We offer healthy relationship education, and financial stability. We also touch on workforce development. These workshops are for couples only.

We are in five locations, so we need a flyer that we can change the text to be able to update the address, dates and any additional information based on our needs.

Attached is the logo we would like to use. I have also attached a previous flyer that we created to give you an idea of the text that is included.

Target Market(s)

We are reaching out to low income adult couples

Font styles to use
Serif

Requirements
Must have
• This flyer must catch the eye of couples wanting to improve their relationship, and finances.
Nice to have
• Some space for us to plug in dates location and times. This flyer also has to have our funding statement at the bottom.

```html
<!DOCTYPE html>
<html lang="es">
<head>
<meta charset="utf-8">
<title>Talleres Para Parejas — Brightfern Couples Unity Program</title>
<link rel="stylesheet" href="https://fonts.googleapis.com/css2?family=Montserrat:wght@700;800&family=Roboto+Condensed:wght@300;400;700&family=Lato:wght@400;700&display=swap">
<style>
  :root {
    --navy: #0f3760;
    --orange: #f18a1c;
    --ink: #3f3f3f;
    --muted: #555;
    --panel: #f2f2f3;
    --page: #e8e5e1;
    --photo-a: #e9dccb;
    --photo-b: #cfd7c6;
    --photo-c: #f6f3ee;
  }
  * { margin: 0; padding: 0; box-sizing: border-box; }
  html, body { width: 1200px; height: 1200px; overflow: hidden; background: var(--page); }
  .flyer {
    position: absolute; left: 190px; top: 20px;
    width: 820px; height: 1160px; background: #fff; overflow: hidden;
    box-shadow: 0 2px 10px rgba(0,0,0,.15);
  }
  .flyer-art { position: absolute; inset: 0; }
  .brand {
    position: absolute; right: 38px; top: 76px; width: 280px; text-align: center;
  }
  .brand-mark {
    display: block; width: 30px; height: 30px; border-radius: 50%;
    background: var(--orange); margin: 0 auto 8px;
  }
  .brand-name {
    font: 400 21px/1.1 "Roboto Condensed", sans-serif; color: var(--orange);
  }
  .brand-tagline {
    margin-top: 5px; font: 700 8.6px/1.35 "Lato", sans-serif;
    color: var(--navy); text-transform: uppercase; letter-spacing: .3px;
  }
  .locations { position: absolute; left: 34px; top: 580px; width: 280px; }
  .locations-heading {
    font: 300 23px/27px "Roboto Condensed", sans-serif; color: #3a3a3a;
  }
  .location-list { list-style: none; margin-top: 20px; }
  .location { position: relative; padding-left: 16px; height: 60px; }
  .location .pin { position: absolute; left: 0; top: 3px; width: 10px; height: 14px; }
  .location-name { font: 400 12.5px/15px "Roboto Condensed", sans-serif; color: #222; }
  .location-address { font: 300 12px/15px "Roboto Condensed", sans-serif; color: #333; }
  .location-date { font: 400 12px/18px "Roboto Condensed", sans-serif; color: #222; }
  .location-date b { color: var(--orange); font-weight: 400; }
  .partners {
    position: absolute; left: 34px; top: 1000px; width: 270px;
    display: flex; justify-content: space-between; align-items: center;
  }
  .partner { font: 700 11px/1.2 "Roboto Condensed", sans-serif; text-align: center; width: 120px; }
  .partner-navy { color: var(--navy); }
  .partner-orange { color: var(--orange); }
  .workshop { position: absolute; left: 330px; top: 562px; width: 460px; text-align: center; }
  .workshop-title {
    font: 800 40px/48px "Montserrat", sans-serif; color: var(--navy); letter-spacing: .3px;
  }
  .workshop-lede {
    margin-top: 10px; font: 300 20px/25px "Roboto Condensed", sans-serif; color: #333;
  }
  .workshop-perk {
    margin-top: 14px; font: 400 19px/24px "Roboto Condensed", sans-serif; color: #222;
    display: flex; justify-content: center; align-items: center; gap: 8px;
  }
  .perk-icon { width: 24px; height: 24px; }
  .topics { position: absolute; left: 338px; top: 752px; width: 442px; }
  .topics-heading {
    display: flex; align-items: center; gap: 10px;
    font: 700 15px/20px "Lato", sans-serif; color: var(--navy); letter-spacing: .4px;
  }
  .topics-heading::before, .topics-heading::after {
    content: ""; flex: 1; height: 1px; background: #9a9a9a;
  }
  .topic-columns { display: flex; margin-top: 16px; gap: 10px; }
  .topic-list { list-style: none; }
  .topic-list.first { width: 222px; }
  .topic-list li {
    display: flex; align-items: center; gap: 8px;
    font: 400 11.5px/19.5px "Lato", sans-serif; color: var(--ink);
  }
  .topic-list.second li { line-height: 24.5px; }
  .tick { width: 11px; height: 11px; flex: none; }
  .topics-rule { margin-top: 12px; height: 1px; background: #9a9a9a; }
  .register { position: absolute; left: 330px; top: 924px; width: 460px; text-align: center; }
  .register-call { font: 400 16.5px/20px "Roboto Condensed", sans-serif; color: var(--navy); }
  .register-info {
    margin-top: 8px; font: 300 13.5px/17px "Roboto Condensed", sans-serif; color: #333;
  }
  .register-phone {
    margin-top: 5px; font: 700 16px/20px "Roboto Condensed", sans-serif; color: var(--orange);
    display: flex; justify-content: center; align-items: center; gap: 5px;
  }
  .phone-icon { width: 14px; height: 14px; }
  .funding {
    position: absolute; left: 48px; right: 48px; top: 1098px;
    font: 400 11.3px/15px "Lato", sans-serif; color: #fff; text-align: left;
  }
</style>
</head>
<body>
<main class="flyer">
  <svg class="flyer-art" width="820" height="1160" viewBox="0 0 820 1160">
    <defs>
      <linearGradient id="photoTone" x1="0" y1="0" x2="1" y2="1">
        <stop offset="0" stop-color="var(--photo-b)"/>
        <stop offset=".45" stop-color="var(--photo-a)"/>
        <stop offset="1" stop-color="var(--photo-c)"/>
      </linearGradient>
      <linearGradient id="panelTone" x1="0" y1="0" x2="1" y2="0">
        <stop offset="0" stop-color="#ffffff"/>
        <stop offset=".7" stop-color="#f3f3f4"/>
        <stop offset="1" stop-color="#e9e9eb"/>
      </linearGradient>
    </defs>
    <rect class="location-panel" x="0" y="520" width="312" height="540" fill="url(#panelTone)"/>
    <path class="side-band" fill="var(--navy)"
      d="M0 0 H95 C70 140 140 230 110 340 C90 420 120 470 170 500 C100 520 30 560 0 600 Z"/>
    <path role="img" aria-label="Photo of a smiling young couple sitting close together on a light sofa"
      fill="url(#photoTone)"
      d="M95 0 H820 V385 C740 470 560 500 330 495 C260 495 210 498 170 500 C120 470 90 420 110 340 C140 230 70 140 95 0 Z"/>
    <path class="photo-edge" fill="none" stroke="var(--orange)" stroke-width="5"
      d="M95 0 C70 140 140 230 110 340 C90 420 120 470 170 500"/>
    <path class="photo-edge" fill="none" stroke="var(--orange)" stroke-width="8"
      d="M0 600 C40 555 110 510 200 502 C300 494 420 505 560 498 C700 490 780 430 820 380"/>
    <path class="footer-band" fill="var(--navy)"
      d="M0 1088 C200 1050 420 1045 600 1052 C700 1056 770 1068 820 1078 V1160 H0 Z"/>
    <path class="footer-edge" fill="none" stroke="var(--orange)" stroke-width="6"
      d="M0 1084 C200 1046 420 1041 600 1048 C700 1052 770 1064 820 1074"/>
  </svg>

  <header class="brand">
    <span class="brand-mark"></span>
    <div class="brand-name">Brightfern Couples Unity Program</div>
    <div class="brand-tagline">Fortalecimiento de relaciones | Capacitación financiera<br>y preparación laboral</div>
  </header>

  <section class="locations">
    <h2 class="locations-heading">Services are currently at the<br>FOLLOWING LOCATIONS:</h2>
    <ul class="location-list">
      <li class="location">
        <svg class="pin" viewBox="0 0 10 14"><path d="M5 0C2.2 0 0 2.2 0 5c0 3.5 5 9 5 9s5-5.5 5-9c0-2.8-2.2-5-5-5zm0 7a2 2 0 110-4 2 2 0 010 4z" fill="var(--navy)"/></svg>
        <div class="location-name">Cedar Hollow Family Resource Center</div>
        <div class="location-address">410 N. Maple Row, Cedar Hollow, CA 90000</div>
        <div class="location-date"><b>DATE</b> : xx.xx.xxxx</div>
      </li>
      <li class="location">
        <svg class="pin" viewBox="0 0 10 14"><path d="M5 0C2.2 0 0 2.2 0 5c0 3.5 5 9 5 9s5-5.5 5-9c0-2.8-2.2-5-5-5zm0 7a2 2 0 110-4 2 2 0 010 4z" fill="var(--navy)"/></svg>
        <div class="location-name">Linden Park Family Resource Center</div>
        <div class="location-address">2250 West Grove Ave., Linden Park, CA 90001</div>
        <div class="location-date"><b>DATE</b> : xx.xx.xxxx</div>
      </li>
      <li class="location">
        <svg class="pin" viewBox="0 0 10 14"><path d="M5 0C2.2 0 0 2.2 0 5c0 3.5 5 9 5 9s5-5.5 5-9c0-2.8-2.2-5-5-5zm0 7a2 2 0 110-4 2 2 0 010 4z" fill="var(--navy)"/></svg>
        <div class="location-name">Harbor Lane Family Resource Center</div>
        <div class="location-address">875 E. Harbor Lane, Bayview, CA 90002</div>
        <div class="location-date"><b>DATE</b> : xx.xx.xxxx</div>
      </li>
      <li class="location">
        <svg class="pin" viewBox="0 0 10 14"><path d="M5 0C2.2 0 0 2.2 0 5c0 3.5 5 9 5 9s5-5.5 5-9c0-2.8-2.2-5-5-5zm0 7a2 2 0 110-4 2 2 0 010 4z" fill="var(--navy)"/></svg>
        <div class="location-name">Sunridge Community Family Resource Center</div>
        <div class="location-address">3120 Ridge Ave., Sunridge, CA 90003</div>
        <div class="location-date"><b>DATE</b> : xx.xx.xxxx</div>
      </li>
      <li class="location">
        <svg class="pin" viewBox="0 0 10 14"><path d="M5 0C2.2 0 0 2.2 0 5c0 3.5 5 9 5 9s5-5.5 5-9c0-2.8-2.2-5-5-5zm0 7a2 2 0 110-4 2 2 0 010 4z" fill="var(--navy)"/></svg>
        <div class="location-name">Valley Oaks Family Resource Center</div>
        <div class="location-address">6045 Oakmont Street, Valley Oaks, CA 90004</div>
        <div class="location-date"><b>DATE</b> : xx.xx.xxxx</div>
      </li>
    </ul>
  </section>

  <footer class="partners">
    <div class="partner partner-navy">Lumen Community Partners</div>
    <div class="partner partner-orange">Willowbend Family Resource Center</div>
  </footer>

  <section class="workshop">
    <h1 class="workshop-title">Talleres Para Parejas</h1>
    <p class="workshop-lede">Porque una relación sana esta<br>“A Nuestro Alcance”</p>
    <p class="workshop-perk">
      <svg class="perk-icon" viewBox="0 0 24 24"><circle cx="12" cy="12" r="11" fill="none" stroke="var(--navy)" stroke-width="1.3"/><circle cx="8.5" cy="7.5" r="1.8" fill="var(--orange)"/><circle cx="15.5" cy="7.5" r="1.8" fill="var(--orange)"/><rect x="7" y="10" width="3" height="8" rx="1" fill="var(--orange)"/><rect x="14" y="10" width="3" height="8" rx="1" fill="var(--orange)"/></svg>
      Cuidado de niños y cena será proporcionado
    </p>
  </section>

  <section class="topics">
    <h2 class="topics-heading">TEMAS INCLUYEN:</h2>
    <div class="topic-columns">
      <ul class="topic-list first">
        <li><svg class="tick" viewBox="0 0 12 12"><circle cx="6" cy="6" r="5.2" fill="none" stroke="var(--navy)" stroke-width="1.2"/><path d="M3.4 6.2l1.8 1.7 3.4-3.6" fill="none" stroke="var(--navy)" stroke-width="1.3"/></svg>Llaves para la buena communicación</li>
        <li><svg class="tick" viewBox="0 0 12 12"><circle cx="6" cy="6" r="5.2" fill="none" stroke="var(--navy)" stroke-width="1.2"/><path d="M3.4 6.2l1.8 1.7 3.4-3.6" fill="none" stroke="var(--navy)" stroke-width="1.3"/></svg>Tipos de personalidad y expectativas</li>
        <li><svg class="tick" viewBox="0 0 12 12"><circle cx="6" cy="6" r="5.2" fill="none" stroke="var(--navy)" stroke-width="1.2"/><path d="M3.4 6.2l1.8 1.7 3.4-3.6" fill="none" stroke="var(--navy)" stroke-width="1.3"/></svg>Señales de peligro en una relación</li>
        <li><svg class="tick" viewBox="0 0 12 12"><circle cx="6" cy="6" r="5.2" fill="none" stroke="var(--navy)" stroke-width="1.2"/><path d="M3.4 6.2l1.8 1.7 3.4-3.6" fill="none" stroke="var(--navy)" stroke-width="1.3"/></svg>Técnicas para formar y sostener una</li>
        <li><svg class="tick" viewBox="0 0 12 12"><circle cx="6" cy="6" r="5.2" fill="none" stroke="var(--navy)" stroke-width="1.2"/><path d="M3.4 6.2l1.8 1.7 3.4-3.6" fill="none" stroke="var(--navy)" stroke-width="1.3"/></svg>relación sana</li>
      </ul>
      <ul class="topic-list second">
        <li><svg class="tick" viewBox="0 0 12 12"><circle cx="6" cy="6" r="5.2" fill="none" stroke="var(--navy)" stroke-width="1.2"/><path d="M3.4 6.2l1.8 1.7 3.4-3.6" fill="none" stroke="var(--navy)" stroke-width="1.3"/></svg>Resolucion de problemas</li>
        <li><svg class="tick" viewBox="0 0 12 12"><circle cx="6" cy="6" r="5.2" fill="none" stroke="var(--navy)" stroke-width="1.2"/><path d="M3.4 6.2l1.8 1.7 3.4-3.6" fill="none" stroke="var(--navy)" stroke-width="1.3"/></svg>Como mantener la diversion</li>
        <li><svg class="tick" viewBox="0 0 12 12"><circle cx="6" cy="6" r="5.2" fill="none" stroke="var(--navy)" stroke-width="1.2"/><path d="M3.4 6.2l1.8 1.7 3.4-3.6" fill="none" stroke="var(--navy)" stroke-width="1.3"/></svg>Como adminstrar el dinero entre pareja</li>
        <li><svg class="tick" viewBox="0 0 12 12"><circle cx="6" cy="6" r="5.2" fill="none" stroke="var(--navy)" stroke-width="1.2"/><path d="M3.4 6.2l1.8 1.7 3.4-3.6" fill="none" stroke="var(--navy)" stroke-width="1.3"/></svg>Y muchos mas</li>
      </ul>
    </div>
    <div class="topics-rule"></div>
  </section>

  <section class="register">
    <p class="register-call">Registration requerida Llamanos hoy !</p>
    <p class="register-info">Para más información llame a<br>Willowbend Family Resource Center</p>
    <p class="register-phone">
      <svg class="phone-icon" viewBox="0 0 14 14"><path d="M3 1l2 3-1.2 1.3c.8 1.8 2.1 3.1 3.9 3.9L9 8l3 2-1 2.5C6 12.5 1.5 8 1.5 2z" fill="var(--navy)"/></svg>
      (555) 214-0398
    </p>
  </section>

  <p class="funding">“Funding for this project was provided by the National Family Services Agency, Office for Children and Families, Grant: #41AB2297. These services are available to all eligible persons, regardless of race, gender, age, disability, or religion.”</p>
</main>
</body>
</html>
```